Web design for Money Service Business (uncoded)

We need a very basic website with 5-6 pages. Home page, Services, Transfer(How to use our service), About us, Contact us, FAQ
Our company name is Meridale Exchange. We are a company that deals with currency exchange and international money transfer. We do cash exchange and international money transfers to bank accounts all over the world. We offer highly competitive exchange rates so usually attract customers who transfer money over $10,000. Our niche is with larger sums of money, the design needs to be professional and communicate trust, security and stability.

```html
<!DOCTYPE html>
<html lang="en">
<head>
<meta charset="utf-8">
<title>Meridale Exchange</title>
<link href="https://fonts.googleapis.com/css2?family=Open+Sans:wght@400;600;700&family=Roboto:wght@400;500&display=swap" rel="stylesheet">
<style>
:root{
  --bg:#e6e6e6;
  --dark:#2b2b2b;
  --darker:#232323;
  --white:#ffffff;
  --blue:#1f5a8c;
  --navy:#1b4f7e;
  --orange:#f7941d;
  --orange-dark:#e07f0c;
  --text:#666666;
  --heading:#333333;
  --grey-box:#6b6b6b;
  --line:#cccccc;
}
*{margin:0;padding:0;box-sizing:border-box}
html,body{width:782px;height:1200px;overflow:hidden}
body{background:var(--bg);font-family:"Open Sans",sans-serif;color:var(--text);position:relative}
.page{position:absolute;left:80px;top:0;width:620px;height:1200px;background:var(--white);overflow:hidden}
.abs{position:absolute}
.topbar{left:0;top:0;width:620px;height:24px;background:var(--dark)}
.phone{left:14px;top:6px;color:#fff;font-size:10px;font-weight:600;display:flex;align-items:center;gap:3px}
.social{display:flex;gap:4px}
.social span{width:13px;height:13px;display:block;border-radius:2px}
.s1{background:#c8232c}.s2{background:#3b5998}.s3{background:#2fa7d8}.s4{background:#6b6b6b}
.topbar .social{position:absolute;left:544px;top:5px}
.brand{left:14px;top:30px}
.brand .name{font-family:"Roboto",sans-serif;font-size:17px;font-weight:500;color:var(--navy);letter-spacing:.5px;line-height:1}
.brand .tag{font-size:5.8px;letter-spacing:1.6px;color:#777;margin-top:3px}
.nav{top:41px;font-size:9px;color:#555}
.nav a{position:absolute;white-space:nowrap;text-decoration:none;color:#555}
.nav a.active{color:var(--orange)}
.hero{left:0;top:62px;width:620px;height:248px;background:radial-gradient(circle at 30% 30%,#b87a4e,transparent 40%),radial-gradient(circle at 75% 60%,#a9a49a,transparent 45%),linear-gradient(135deg,#7e5a3c,#a07654 35%,#8d8a82 60%,#6e5040)}
.cap1{left:13px;top:85px;height:31px;background:rgba(40,30,20,.75);color:var(--orange);font-size:12px;line-height:31px;padding:0 9px;font-family:"Roboto",sans-serif;white-space:nowrap}
.cap2{left:13px;top:119px;height:30px;background:rgba(255,255,255,.85);color:var(--navy);font-size:12px;line-height:30px;padding:0 12px;font-family:"Roboto",sans-serif;white-space:nowrap}
.btn{background:linear-gradient(#fba632,var(--orange-dark));color:#3a2200;font-size:7.5px;font-weight:700;display:flex;align-items:center;justify-content:center;border-radius:2px;box-shadow:0 1px 2px rgba(0,0,0,.25);white-space:nowrap}
.video{left:13px;top:342px;width:248px;height:158px;background:linear-gradient(135deg,#d9d6cf,#9ea48e 50%,#2a2a2a)}
.play{left:106px;top:60px;width:37px;height:37px;background:rgba(20,20,20,.85);border-radius:3px;display:flex;align-items:center;justify-content:center}
h2.about{left:286px;top:339px;font-family:"Roboto",sans-serif;font-size:11.5px;font-weight:500;color:var(--heading)}
.para{font-size:7.2px;line-height:9.3px;color:var(--text)}
.checks{left:286px;top:411px;font-size:7.2px;color:var(--text)}
.checks li{list-style:none;height:19px;display:flex;align-items:center;gap:5px}
.svc-icon{width:50px;height:50px;background:var(--blue);border-radius:3px;display:flex;align-items:center;justify-content:center}
.svc-title{font-family:"Roboto",sans-serif;font-size:10px;color:var(--heading)}
.svc-text{font-size:7.2px;line-height:11px;width:220px;color:var(--text)}
.more{display:inline-block;width:10px;height:10px;border-radius:50%;background:var(--orange);vertical-align:middle;margin-left:4px;position:relative}
.more-dot{position:absolute;display:block;width:10px;height:10px;border-radius:50%;background:var(--orange)}
.more::after,.more-dot::after{content:"";position:absolute;left:3px;top:3px;width:3px;height:3px;border-right:1.5px solid #fff;border-top:1.5px solid #fff;transform:rotate(45deg)}
.sec-h{font-family:"Roboto",sans-serif;font-size:12.5px;font-weight:500;color:var(--heading);border-bottom:1px solid var(--line);padding-bottom:3px}
.news-img{width:70px;height:52px;background:linear-gradient(135deg,#cfdbe6,#6f8fb0)}
.news-img.b{background:linear-gradient(135deg,#e3ddd0,#3a3a3a)}
.news-title{font-size:8.5px;font-weight:700;color:var(--navy)}
.news-text{font-size:7.2px;line-height:9.3px;width:186px}
.portrait{left:292px;top:748px;width:118px;height:154px;background:linear-gradient(#f4f4f4,#c7d9ea)}
.quote{left:408px;top:765px;width:198px;height:61px;background:var(--grey-box);color:#eee;font-size:7.2px;line-height:9.3px;padding:11px 10px}
.quote::after{content:"";position:absolute;left:10px;bottom:-9px;border-right:10px solid transparent;border-top:9px solid var(--grey-box)}
.member{left:14px;top:922px;width:594px;height:63px;background:var(--blue);overflow:hidden}
.member .lead{position:absolute;left:10px;top:22px;color:#fff;font-size:13.5px;font-family:"Roboto",sans-serif;white-space:nowrap}
.member .deal{position:absolute;left:150px;top:0;width:90px;height:63px;background:var(--orange);transform:skewX(-14deg)}
.member .pct{position:absolute;left:160px;top:10px;width:70px;text-align:center;color:#fff;line-height:1}
.member .pct b{display:block;font-family:"Roboto",sans-serif;font-weight:400;font-size:24px}
.member .pct i{font-style:normal;font-size:11px;font-weight:600}
.member .mb{position:absolute;left:242px;top:12px;color:#fff;font-size:9px;font-weight:700}
.member .bf{position:absolute;color:#fff;font-size:7.2px;display:flex;align-items:center;gap:3px;white-space:nowrap}
.footer{left:0;top:1010px;width:620px;height:156px;background:var(--dark)}
.bottom{left:0;top:1166px;width:620px;height:34px;background:var(--darker)}
.f-name{font-family:"Roboto",sans-serif;font-size:17px;font-weight:500;color:var(--navy);line-height:1;white-space:nowrap}
.f-text{color:#ddd;font-size:6px;line-height:11px;width:140px}
.f-nav a{display:block;color:#eee;font-size:9px;height:19.2px;text-decoration:none}
.f-nav a.active{color:var(--orange)}
.f-h{color:#fff;font-size:8.5px;font-weight:700}
.photos{display:grid;grid-template-columns:repeat(3,36px);grid-template-rows:repeat(2,36px);gap:3px}
.photos span{display:block}
.f-contact{color:#eee;font-size:5.8px;white-space:nowrap}
.f-contact p{height:22.5px}
</style>
</head>
<body>
<div class="page">
  <header>
    <div class="abs topbar">
      <div class="abs phone">
        <svg width="8" height="10" viewBox="0 0 8 10"><path d="M2 0 L4 2 L3 4 Q4 6 5.5 7 L6.5 6 L8 8 L6.5 10 Q1 8 0.5 1 Z" fill="#f7941d"/></svg>
        1-800-555-0142
      </div>
      <div class="social" aria-label="Social links"><span class="s1"></span><span class="s2"></span><span class="s3"></span><span class="s4"></span></div>
    </div>
    <div class="abs brand">
      <div class="name">MERIDALE EXCHANGE</div>
      <div class="tag">INTERNATIONAL MONEY TRANSFER</div>
    </div>
    <nav class="abs nav">
      <a class="active" style="left:339px">Home</a>
      <a style="left:379px">Services</a>
      <a style="left:429px">Transfer</a>
      <a style="left:479px">About us</a>
      <a style="left:531px">Contact us</a>
      <a style="left:590px">FAQ</a>
    </nav>
  </header>

  <section class="abs hero" role="img" aria-label="Pile of assorted coins from many currencies">
    <div class="abs cap1">Lorem ipsum dolor sit amet consectetur</div>
    <div class="abs cap2">Adipisicing elit sed do</div>
    <div class="abs btn" style="left:13px;top:181px;width:73px;height:21px">Read more</div>
  </section>

  <section>
    <div class="abs video" role="img" aria-label="Video still of hands counting banknotes">
      <div class="abs play"><svg width="16" height="18" viewBox="0 0 16 18"><path d="M1 1 L15 9 L1 17 Z" fill="#fff"/></svg></div>
    </div>
    <h2 class="abs about">About our company</h2>
    <p class="abs para" style="left:286px;top:358px;width:318px">Lorem ipsum dolor sit amet, consectetur adipisicing elit, sed do eiusmod tempor incididunt ut labore et dolore magna aliqua. Ut enim ad minim veniam, quis nostrud exercitation ullamco laboris nisi ut aliquip ex ea commodo consequat. Duis aute irure dolor in reprehenderit in voluptate velit esse cillum dolore eu fugiat nulla pariatur. Excepteur sint</p>
    <ul class="abs checks">
      <li><svg width="10" height="9" viewBox="0 0 10 9"><path d="M1 5 L4 8 L9 1" stroke="#1f5a8c" stroke-width="2" fill="none"/></svg>Lorem ipsum dolor sit amet, consectetur adipisicing</li>
      <li><svg width="10" height="9" viewBox="0 0 10 9"><path d="M1 5 L4 8 L9 1" stroke="#1f5a8c" stroke-width="2" fill="none"/></svg>elit, sed do eiusmod tempor incididunt ut labore et</li>
      <li><svg width="10" height="9" viewBox="0 0 10 9"><path d="M1 5 L4 8 L9 1" stroke="#1f5a8c" stroke-width="2" fill="none"/></svg>dolore magna aliqua.</li>
    </ul>
    <div class="abs btn" style="left:286px;top:478px;width:74px;height:21px">Read more</div>
  </section>

  <section class="services">
    <div class="abs svc-icon" style="left:14px;top:544px"><svg width="36" height="30" viewBox="0 0 36 30"><path d="M4 9 H30 M24 3 L31 9 L24 15 M32 21 H6 M12 15 L5 21 L12 27" stroke="#fff" stroke-width="3.5" fill="none"/></svg></div>
    <div class="abs svc-title" style="left:69px;top:543px">Money Exchange</div>
    <p class="abs svc-text" style="left:69px;top:560px">Lorem ipsum dolor sit amet, consectetur adipisicing elit, sed eiusmod tempor incididunt ut labore et dolore magna aliqua. enim ad minim veniam<span class="more"></span></p>

    <div class="abs svc-icon" style="left:339px;top:544px"><svg width="38" height="38" viewBox="0 0 38 38"><circle cx="19" cy="19" r="16" stroke="#fff" stroke-width="3.5" fill="none"/><text x="19" y="27" text-anchor="middle" font-family="Open Sans,sans-serif" font-size="22" font-weight="700" fill="#fff">$</text></svg></div>
    <div class="abs svc-title" style="left:395px;top:543px">Money Transfer</div>
    <p class="abs svc-text" style="left:396px;top:558px">Lorem ipsum dolor sit amet, consectetur adipisicing elit, sed eiusmod tempor incididunt ut labore et dolore magna aliqua. enim ad minim veniam<span class="more"></span></p>

    <div class="abs svc-icon" style="left:14px;top:622px"><svg width="30" height="34" viewBox="0 0 30 34"><rect x="6" y="6" width="14" height="24" rx="2" stroke="#fff" stroke-width="2" fill="none"/><path d="M22 2 Q27 2 27 7 M22 5 Q24 5 24 7" stroke="#fff" stroke-width="1.5" fill="none"/></svg></div>
    <div class="abs svc-title" style="left:70px;top:621px">Mobile Tranfer</div>
    <p class="abs svc-text" style="left:69px;top:639px">Lorem ipsum dolor sit amet, consectetur adipisicing elit, sed eiusmod tempor incididunt ut labore et dolore magna aliqua. enim ad minim veniam<span class="more"></span></p>

    <div class="abs svc-icon" style="left:339px;top:622px"><svg width="40" height="30" viewBox="0 0 40 30"><circle cx="20" cy="15" r="3.5" fill="#fff"/><path d="M13 8 Q9 15 13 22 M27 8 Q31 15 27 22 M7 3 Q0 15 7 27 M33 3 Q40 15 33 27" stroke="#fff" stroke-width="3" fill="none"/></svg></div>
    <div class="abs svc-title" style="left:395px;top:622px">Online Money Tranfer</div>
    <p class="abs svc-text" style="left:396px;top:639px">Lorem ipsum dolor sit amet, consectetur adipisicing elit, sed eiusmod tempor incididunt ut labore et dolore magna aliqua. enim ad minim veniam<span class="more"></span></p>
  </section>

  <section class="news">
    <h3 class="abs sec-h" style="left:13px;top:719px;width:261px">News</h3>
    <div class="abs news-img" style="left:14px;top:757px" role="img" aria-label="Man working on a laptop"></div>
    <div class="abs news-title" style="left:93px;top:754px">Lorem ipsum dolor</div>
    <p class="abs news-text" style="left:93px;top:768px">Lorem ipsum dolor sit amet, consectetur adipisicing elit, sed do eiusmod tempor incididunt ut labore et dolore magna aliqua. Ut enim ad minim veniam, quis</p>
    <span class="more-dot" style="left:94px;top:799px"></span>
    <div class="abs news-img b" style="left:14px;top:834px" role="img" aria-label="Graduate in cap and gown"></div>
    <div class="abs news-title" style="left:93px;top:830px">Lorem ipsum dolor</div>
    <p class="abs news-text" style="left:93px;top:844px">Lorem ipsum dolor sit amet, consectetur adipisicing elit, sed do eiusmod tempor incididunt ut labore et dolore magna aliqua. Ut enim ad minim veniam, quis</p>
    <span class="more-dot" style="left:94px;top:875px"></span>
  </section>

  <section class="testimonials">
    <h3 class="abs sec-h" style="left:317px;top:720px;width:289px">Testimonials</h3>
    <div class="abs portrait" role="img" aria-label="Portrait of a smiling client in a light blue shirt"></div>
    <div class="abs quote">Lorem ipsum dolor sit amet, consectetur adipisicing elit, sed do eiusmod tempor incididunt ut labore et dolore magna aliqua. Ut enim ad minim veniam, quis nostrud exercitation ullamco laboris nisi ut aliquip ex</div>
    <div class="abs" style="left:423px;top:848px;font-size:10px;color:var(--navy)">Daniel <span style="font-size:7.2px;color:#555">Manager</span></div>
  </section>

  <section class="abs member">
    <div class="lead">Be a Member and get</div>
    <div class="deal"></div>
    <div class="pct"><b>10%</b><i>discount</i></div>
    <div class="mb">More Benefits</div>
    <div class="bf" style="left:242px;top:28px"><svg width="9" height="9" viewBox="0 0 9 9"><rect x="0.5" y="1.5" width="7" height="7" stroke="#f7941d" fill="none"/><path d="M2 4 L4 6.5 L8.5 0.5" stroke="#f7941d" stroke-width="1.5" fill="none"/></svg>Lorem ipsum dolor sit amet</div>
    <div class="bf" style="left:242px;top:41px"><svg width="9" height="9" viewBox="0 0 9 9"><rect x="0.5" y="1.5" width="7" height="7" stroke="#f7941d" fill="none"/><path d="M2 4 L4 6.5 L8.5 0.5" stroke="#f7941d" stroke-width="1.5" fill="none"/></svg>consectetur adipiscing elit</div>
    <div class="bf" style="left:363px;top:28px"><svg width="9" height="9" viewBox="0 0 9 9"><rect x="0.5" y="1.5" width="7" height="7" stroke="#f7941d" fill="none"/><path d="M2 4 L4 6.5 L8.5 0.5" stroke="#f7941d" stroke-width="1.5" fill="none"/></svg>sed do eiusmod tempor</div>
    <div class="bf" style="left:363px;top:41px"><svg width="9" height="9" viewBox="0 0 9 9"><rect x="0.5" y="1.5" width="7" height="7" stroke="#f7941d" fill="none"/><path d="M2 4 L4 6.5 L8.5 0.5" stroke="#f7941d" stroke-width="1.5" fill="none"/></svg>Ut enim ad minim veniam,</div>
    <div class="abs btn" style="left:482px;top:26px;width:102px;height:20px">Get you discount now</div>
  </section>

  <footer>
    <div class="abs footer">
      <div class="abs" style="left:14px;top:30px">
        <div class="f-name">MERIDALE EXCHANGE</div>
        <div style="font-size:5.8px;letter-spacing:1.6px;color:#999;margin-top:3px">INTERNATIONAL MONEY TRANSFER</div>
      </div>
      <p class="abs f-text" style="left:14px;top:60px">Lorem ipsum dolor sit amet, consectetur adipiscing elit. Donec iaculis metus vitae ligula elementum ut luctus lorem facilisis. Sed non leo nisl, ac euismod nisl. Aenean augue dolor, facilisis id fringilla ut, tempus vitae nibh. Nullam nec diam risus.</p>
      <nav class="abs f-nav" style="left:221px;top:32px">
        <a class="active">Home</a><a>Services</a><a>Transfer</a><a>About us</a><a>Contact us</a><a>FAQ</a>
      </nav>
      <div class="abs f-h" style="left:342px;top:32px">PHOTOSTREAM.</div>
      <div class="abs photos" style="left:344px;top:60px" role="img" aria-label="Photo thumbnails gallery">
        <span style="background:#a8a29a"></span><span style="background:#7a7a7a"></span><span style="background:#8c5a4a"></span>
        <span style="background:#6a6a66"></span><span style="background:#c7a94a"></span><span style="background:#9a9388"></span>
      </div>
      <div class="abs f-h" style="left:524px;top:32px">CONTACT INFO.</div>
      <div class="abs f-contact" style="left:524px;top:60px">
        <p>48 Harbor Ln, Easton 20417</p>
        <p>+2-12-5550187</p>
        <p>hello@meridale.example</p>
        <p>www.meridale.example</p>
      </div>
    </div>
    <div class="abs bottom">
      <div class="abs" style="left:14px;top:13px;color:#ddd;font-size:7.2px">© 2013, Copy Right for Meridale Exchange</div>
      <div class="social abs" style="left:544px;top:11px"><span class="s1"></span><span class="s2"></span><span class="s3"></span><span class="s4"></span></div>
    </div>
  </footer>
</div>
</body>
</html>
```